Garten- und Landschaftsbaufirma sucht Design
Zielgruppe
Tätigkeiten der Firma:
- Pflasterarbeiten mit Beton- und Naturstein
- Erdbauarbeiten
- Terrassenbau
- Mauerbau
- Zaun- und Sichtschutzbau
- Rodungen
- Rückschnittarbeiten
- Stauden- und Gehölzpflege
- Baumpflege
- Pflanzungen
- Holzbauarbeiten
- Und noch viele mehr…
Zielgruppe: vermögende Privatkundschaft und Unternehmen
Aufgabenstellung
Erstellung eines unverwechselbaren Logo / Corporate Design sowie einer übersichtlichen Website, die Attribute wie Exklusivität, Leidenschaft, Vertrauen, Qualität, Kreativität, Beharrlichkeit, Ausdauer, Verantwortungsbewusstsein sowie fachliche Kompetenz ausstrahlt.
Design passend zur Lackierung der neuen Firmenfahrzeuge (RAL 6010)
Website wie z.B. die der Firma "Brommelt" .
http://www.brommelt-beispiel.de/start.html

```html
<!DOCTYPE html>
<html lang="de">
<head>
<meta charset="utf-8">
<title>Gartengestaltung Wendrich GmbH – Corporate Design</title>
<link rel="stylesheet" href="https://fonts.googleapis.com/css2?family=Montserrat:wght@400;500;600;700&display=swap">
<style>
  :root {
    --bg: #e8eed9;
    --bg-light: #eef3e3;
    --green: #2e8a35;
    --green-dark: #1f5a22;
    --olive: #7f8f3a;
    --orange: #e9884d;
    --ink: #3f3f3f;
    --ink-soft: #666;
    --paper: #ffffff;
    --shadow: 0 4px 14px rgba(60, 80, 40, 0.18);
    --brand-gradient: linear-gradient(135deg, var(--green) 0%, var(--olive) 55%, var(--orange) 100%);
  }
  * { box-sizing: border-box; margin: 0; padding: 0; }
  html, body {
    width: 1200px; height: 791px; overflow: hidden;
    font-family: "Montserrat", Arial, sans-serif;
    color: var(--ink);
  }
  .canvas {
    position: relative; width: 1200px; height: 791px;
    background: radial-gradient(ellipse at 60% 45%, var(--bg-light), var(--bg) 70%);
  }

  /* ---------- guide column ---------- */
  .guide { position: absolute; left: 73px; top: 48px; width: 320px; }
  .guide-title { font-size: 23px; font-weight: 400; letter-spacing: 0.3px; }
  .guide-title strong { font-weight: 700; }
  .guide-rule {
    width: 94px; height: 2px; margin-top: 4px;
    background: linear-gradient(90deg, var(--green), var(--orange));
  }

  .wordmark { display: flex; align-items: center; gap: 14px; }
  .wordmark-dot { border-radius: 50%; background: var(--green-dark); flex: none; }
  .wordmark-text { font-weight: 500; color: var(--ink); line-height: 1.15; text-transform: uppercase; }
  .wordmark-text span { display: block; }

  .wordmark--wide { margin-top: 40px; }
  .wordmark--wide .wordmark-dot { width: 58px; height: 58px; }
  .wordmark--wide .wordmark-text { font-size: 12.5px; letter-spacing: 0.4px; }
  .wordmark--wide .wordmark-text span + span { font-size: 15.5px; }

  .wordmark--stacked { flex-direction: column; gap: 14px; margin: 52px 0 0 32px; width: 130px; }
  .wordmark--stacked .wordmark-dot { width: 62px; height: 62px; }
  .wordmark--stacked .wordmark-text { font-size: 11px; text-align: center; letter-spacing: 0.3px; }
  .wordmark--stacked .wordmark-text span + span { font-size: 14px; }

  .type-section { margin-top: 132px; }
  .type-sample { margin-top: 26px; }
  .type-sample-word { font-size: 22px; font-weight: 400; letter-spacing: 0.4px; }
  .type-sample-weight { font-size: 14px; font-weight: 500; margin-top: 6px; color: var(--ink-soft); }
  .type-sample--semibold .type-sample-word { font-weight: 600; font-size: 22px; }
  .type-sample--semibold .type-sample-weight { font-weight: 600; color: var(--ink); }

  /* ---------- stationery ---------- */
  .piece { position: absolute; background: var(--paper); box-shadow: var(--shadow); }

  .letterhead { left: 430px; top: 36px; width: 240px; height: 340px; }
  .letterhead-sender { position: absolute; left: 18px; top: 18px; font-size: 4.5px; color: var(--ink-soft); }
  .letterhead .mini-mark { position: absolute; right: 18px; top: 40px; }
  .letterhead-footer {
    position: absolute; left: 18px; right: 18px; bottom: 20px;
    border-top: 1px solid transparent;
    border-image: linear-gradient(90deg, var(--green), var(--orange)) 1;
    padding-top: 7px; display: flex; justify-content: space-between;
    font-size: 4.3px; line-height: 1.55; color: var(--ink-soft);
  }
  .letterhead-footer strong { color: var(--green-dark); font-weight: 600; }

  .mini-mark { display: flex; align-items: center; gap: 4px; }
  .mini-mark .wordmark-dot { width: 12px; height: 12px; }
  .mini-mark .wordmark-text { font-size: 4.6px; }
  .mini-mark .wordmark-text span + span { font-size: 5.6px; }

  .folder { left: 700px; top: 36px; width: 250px; height: 340px; overflow: hidden; }
  .folder-image { position: absolute; inset: 0; background: var(--brand-gradient); }
  .reverse-mark { position: absolute; display: flex; align-items: center; gap: 6px; color: #fff; }
  .reverse-mark .wordmark-dot { background: #fff; }
  .reverse-mark .wordmark-text { color: #fff; }
  .folder .reverse-mark { right: 20px; top: 120px; }
  .folder .wordmark-dot { width: 16px; height: 16px; }
  .folder .wordmark-text { font-size: 5.5px; }
  .folder .wordmark-text span + span { font-size: 7px; }

  .card { width: 180px; height: 116px; }
  .card--front { left: 980px; top: 36px; padding: 14px 14px; }
  .card-name { font-size: 8px; font-weight: 600; color: var(--green-dark); }
  .card-rule { width: 40px; height: 1px; margin: 5px 0 6px; background: linear-gradient(90deg, var(--green), var(--orange)); }
  .card-contact { font-size: 5.4px; line-height: 1.6; color: var(--ink-soft); }
  .card--front .mini-mark { position: absolute; right: 12px; bottom: 12px; }
  .card--back { left: 980px; top: 170px; overflow: hidden; }
  .card--back .folder-image { position: absolute; inset: 0; }
  .card--back .reverse-mark { left: 50%; top: 50%; transform: translate(-50%, -50%); }
  .card--back .wordmark-dot { width: 14px; height: 14px; }
  .card--back .wordmark-text { font-size: 5px; white-space: nowrap; }
  .card--back .wordmark-text span + span { font-size: 6.5px; }

  .envelope { left: 430px; top: 420px; width: 520px; height: 260px; }
  .envelope-flap {
    position: absolute; left: 0; right: 0; top: 0; height: 34px;
    background: linear-gradient(90deg, var(--green), var(--olive) 55%, var(--orange));
    border-radius: 0 0 18px 18px;
  }
  .envelope-sender { position: absolute; left: 28px; top: 56px; }
  .envelope-sender .wordmark-text { font-size: 10px; letter-spacing: 0.5px; }
  .envelope-sender .wordmark-text span + span { font-size: 13px; }
  .envelope .mini-mark { position: absolute; right: 26px; bottom: 22px; gap: 6px; }
  .envelope .mini-mark .wordmark-dot { width: 22px; height: 22px; }
  .envelope .mini-mark .wordmark-text { font-size: 6px; }
  .envelope .mini-mark .wordmark-text span + span { font-size: 7.5px; }
</style>
</head>
<body>
<main class="canvas">

  <section class="guide">
    <h2 class="guide-title">Logo <strong>Verwendung</strong></h2>
    <div class="guide-rule"></div>

    <div class="wordmark wordmark--wide">
      <span class="wordmark-dot"></span>
      <p class="wordmark-text"><span>Gartengestaltung</span><span>Wendrich GmbH</span></p>
    </div>

    <div class="wordmark wordmark--stacked">
      <span class="wordmark-dot"></span>
      <p class="wordmark-text"><span>Gartengestaltung</span><span>Wendrich GmbH</span></p>
    </div>

    <div class="type-section">
      <h2 class="guide-title">Schriftart <strong>Montserrat</strong></h2>
      <div class="guide-rule"></div>
      <div class="type-sample">
        <p class="type-sample-word">Gartengestaltung</p>
        <p class="type-sample-weight">Regular</p>
      </div>
      <div class="type-sample type-sample--semibold">
        <p class="type-sample-word">Wendrich</p>
        <p class="type-sample-weight">Semibold</p>
      </div>
    </div>
  </section>

  <article class="piece letterhead">
    <p class="letterhead-sender">Gartengestaltung Wendrich GmbH · Musterweg 1 · 12345 Musterstadt</p>
    <div class="mini-mark">
      <span class="wordmark-dot"></span>
      <p class="wordmark-text"><span>Gartengestaltung</span><span>Wendrich GmbH</span></p>
    </div>
    <footer class="letterhead-footer">
      <p><strong>Gartengestaltung Wendrich GmbH</strong><br>Musterweg 1<br>12345 Musterstadt</p>
      <p>Tel. 0123 456 789<br>Fax 0123 456 780<br>info@gartengestaltung-wendrich.de</p>
      <p>Musterbank Musterstadt<br>IBAN DE00 1234 5678 90<br>BIC MUSTDE00</p>
    </footer>
  </article>

  <article class="piece folder">
    <div class="folder-image" role="img" aria-label="Foto einer Rose, grün-orange getönt"></div>
    <div class="reverse-mark">
      <span class="wordmark-dot"></span>
      <p class="wordmark-text"><span>Gartengestaltung</span><span>Wendrich GmbH</span></p>
    </div>
  </article>

  <article class="piece card card--front">
    <p class="card-name">Max Mustermann</p>
    <div class="card-rule"></div>
    <p class="card-contact">Musterweg 1<br>12345 Musterstadt<br>Tel. 0123 456 789<br>info@gartengestaltung-wendrich.de<br>www.gartengestaltung-wendrich.de</p>
    <div class="mini-mark">
      <span class="wordmark-dot"></span>
    </div>
  </article>

  <article class="piece card card--back">
    <div class="folder-image" role="img" aria-label="Foto einer Rose, grün-orange getönt"></div>
    <div class="reverse-mark">
      <span class="wordmark-dot"></span>
      <p class="wordmark-text"><span>Gartengestaltung</span><span>Wendrich GmbH</span></p>
    </div>
  </article>

  <article class="piece envelope">
    <div class="envelope-flap"></div>
    <div class="wordmark envelope-sender">
      <p class="wordmark-text"><span>Gartengestaltung</span><span>Wendrich GmbH</span></p>
    </div>
    <div class="mini-mark">
      <span class="wordmark-dot"></span>
      <p class="wordmark-text"><span>Gartengestaltung</span><span>Wendrich GmbH</span></p>
    </div>
  </article>

</main>
</body>
</html>
```